Simple elegant business card

General card for a fin and television director.
Just want name, email, phone and address.

Target Market(s)

Prospective employers

Industry/Entity Type

Business

Requirements
Must have
• As above
Nice to have
• Logo but not necessary.
Should not have
• Not too colourful or funky.
• Simplicity and elegance the way to go.

```html
<!DOCTYPE html>
<html lang="en">
<head>
<meta charset="utf-8">
<title>Nora Banks – Business Card</title>
<link rel="stylesheet" href="https://fonts.googleapis.com/css2?family=Damion&family=Roboto:wght@300&display=swap">
<style>
  :root {
    --backdrop: #c8c8c8;
    --card-burgundy: #51172a;
    --name-pink: #ec8fcb;
    --contact-mauve: #b47c96;
  }
  html, body {
    margin: 0;
    padding: 0;
    width: 1200px;
    height: 1200px;
    overflow: hidden;
    background: var(--backdrop);
  }
  .canvas {
    position: relative;
    width: 1200px;
    height: 1200px;
  }
  .business-card {
    position: absolute;
    left: 100px;
    top: 314px;
    width: 1000px;
    height: 572px;
    background: var(--card-burgundy);
    box-sizing: border-box;
  }
  .card-name {
    position: absolute;
    left: 0;
    right: 0;
    top: 150px;
    margin: 0;
    text-align: center;
    font-family: "Damion", cursive;
    font-weight: 400;
    font-size: 140px;
    line-height: 1;
    color: var(--name-pink);
  }
  .card-contact {
    position: absolute;
    left: 335px;
    top: 318px;
    margin: 0;
    font-family: "Roboto", "Helvetica Neue", Arial, sans-serif;
    font-weight: 300;
    font-size: 33px;
    line-height: 1.15;
    letter-spacing: 0.5px;
    color: var(--contact-mauve);
    font-style: normal;
  }
  .card-contact span {
    display: block;
  }
</style>
</head>
<body>
  <main class="canvas">
    <section class="business-card">
      <h1 class="card-name">Nora Banks</h1>
      <address class="card-contact">
        <span class="contact-email">norabanks@mail.com</span>
        <span class="contact-phone">+1 310 555 0142</span>
      </address>
    </section>
  </main>
</body>
</html>
```